FLYER POSTCARD ADVERT FOR GARNET QUARTER

OUR COMPANY NAME IS TOLVEK DESIGNS.

WE NEED TO MAKE A POSTCARD FRONT AND BACK TO HAND OUT AND MAIL TO LOCAL JEWELERS DESCRIBING OUR WEDDING RING MANUFACTURING AND FINISHING SERVICES.
KEY POINTS WE WOULD LIKE LISTED:

FAST AND RELIABLE CONTRACTORS THAT ARE IN THE WEDDING RING INDUSTRY SINCE 1979

WE OFFER:
SWISS CUTTING
BASIC TO COMPLEX FINISHES AND DESIGNS
HAND CHASING/EMBOSSING AND ENGRAVING
LASER ENGRAVING
DIAMOND SETTING

CUTTING AND FINISHING AS LOW AS $10 PER PIECE

10K - 14K - 18K - PLATINUM - PALLADIUM - .935 SILVER
VOLUME AND SPECIAL ORDERS ACCEPTED
NO MINIMUMS

EMAIL : INFO@TOLVEKDESIGNS.EXAMPLE
TEL: 555 - 314- 9072

Target Market(s)

WHOLESALE JEWELERS

Industry/Entity Type

Jewelry

Font styles to use
Serif

Colors

Designer to choose colors to be used in the design.

Requirements
Must have
• OUR LOGO, WEVE ATTACHED BOTH WHITE AND BLACK BACKGROUND TO USE DEPENDING ON THE COLOR SCHEME.
• ALSO NEEDS THESE KEY POINTS LISTED TOO:
• FAST AND RELIABLE CONTRACTORS AND MANUFACTURERS SERVICING THE WEDDING RING INDUSTRY SINCE 1979
• WE OFFER:
• SWISS CUTTING
• BASIC TO COMPLEX FINISHES AND DESIGNS
• HAND CHASING/EMBOSSING AND ENGRAVING
• LASER ENGRAVING
• DIAMOND SETTING
• CUTTING AND FINISHING AS LOW AS $10 PER PIECE
• 10K - 14K - 18K - PLATINUM - PALLADIUM - .935 SILVER
• VOLUME AND SPECIAL ORDERS ACCEPTED
• NO MINIMUMS
• EMAIL : INFO@TOLVEKDESIGNS.EXAMPLE
• TEL: 555 - 314- 9072
Should not have
• WE DONT MIND COLOR, BUT WE DONT WANT AN EXPLOSION OF COLORS EITHER. WE WOULD LIKE IT TO BE EASY ON THE EYE.

```html
<!DOCTYPE html>
<html lang="en">
<head>
<meta charset="utf-8">
<title>Tolvek Designs – Postcard</title>
<link rel="stylesheet" href="https://fonts.googleapis.com/css2?family=Oswald:wght@300;400;500;600&family=Open+Sans:wght@400;600;700&family=Great+Vibes&display=swap">
<style>
  :root{
    --page:#ecebe8;
    --charcoal:#2c2c2c;
    --gold:#f2b705;
    --gold-deep:#d99a00;
    --gold-light:#ffd75a;
    --white:#ffffff;
  }
  *{box-sizing:border-box;margin:0;padding:0}
  html,body{width:955px;height:1200px;overflow:hidden;background:var(--page)}
  .canvas{position:relative;width:955px;height:1200px}

  .card{position:absolute;left:84px;width:787px;height:506px;overflow:hidden;
        box-shadow:0 3px 8px rgba(0,0,0,.25)}
  .card--front{top:72px;background:var(--charcoal)}
  .card--back{top:620px;background:var(--white)}
  .card__art{position:absolute;inset:0;width:100%;height:100%}

  .brand{position:absolute;font-family:"Oswald",sans-serif;font-weight:400;color:var(--gold);
         text-align:center;white-space:nowrap;line-height:1}
  .brand-dot{position:absolute;border-radius:50%;background:var(--gold)}

  /* front */
  .front__dot{left:599px;top:31px;width:34px;height:34px}
  .front__brand{left:496px;width:240px;top:100px;font-size:24px;letter-spacing:3px}
  .since{position:absolute;left:566px;top:140px;width:100px;height:20px;
         background:linear-gradient(#f4f4f4,#bdbdbd);color:#333;
         font-family:"Open Sans",sans-serif;font-size:13px;line-height:20px;text-align:center}
  .tagline{position:absolute;left:475px;top:178px;width:290px;font-family:"Oswald",sans-serif;
           font-weight:500;font-size:19px;line-height:24px;color:#eaeaea;white-space:nowrap}
  .script{position:absolute;font-family:"Great Vibes",cursive;color:var(--gold);white-space:nowrap;line-height:1}
  .script--line1{left:464px;top:210px;font-size:40px}
  .script--line2{left:546px;top:250px;font-size:54px}
  .provide{position:absolute;left:482px;top:318px;width:132px;height:26px;border-radius:4px;
           background:linear-gradient(var(--gold-light),var(--gold-deep));
           font-family:"Open Sans",sans-serif;font-weight:700;font-size:14.5px;color:#1d1d1d;
           text-align:center;line-height:26px;letter-spacing:.5px}
  .services{position:absolute;left:486px;top:356px;list-style:none;
            font-family:"Open Sans",sans-serif;font-size:12.8px;color:#ececec}
  .services li{position:relative;padding-left:16px;height:22.4px;line-height:22.4px}
  .services li::before{content:"";position:absolute;left:0;top:9px;width:5px;height:5px;
                       border-radius:50%;background:var(--gold)}
  .contact-bar{position:absolute;left:282px;top:482px;right:0;height:24px;display:flex;
               flex-wrap:nowrap;align-items:center;gap:7px;padding-left:14px;white-space:nowrap;
               font-family:"Open Sans",sans-serif;font-size:11px;color:#2a2a2a}
  .contact-bar .sep{width:1px;height:14px;background:#777;flex:none}
  .contact-bar .phone{font-family:"Oswald",sans-serif;font-weight:500;font-size:14px}
  .contact-item{display:flex;align-items:center;gap:5px;white-space:nowrap}
  .icon{width:13px;height:13px;flex:none}

  /* back */
  .offer{position:absolute;left:28px;top:32px;font-family:"Oswald",sans-serif;color:var(--white);white-space:nowrap}
  .offer__lead{font-weight:300;font-size:29px;line-height:36px;display:block}
  .offer__price{font-weight:500;font-size:29px;line-height:36px;display:block}
  .offer__price em{font-style:normal;color:var(--gold);font-size:33px}
  .metal{position:absolute;top:140px;width:96px;height:96px;border-radius:50%;
         border:3px solid var(--gold);padding:4px;background:var(--charcoal)}
  .metal__face{width:100%;height:100%;border-radius:50%;
               background:radial-gradient(circle at 50% 35%,#ffffff,#c9c9c9 70%,#9c9c9c);
               display:flex;flex-direction:column;align-items:center;justify-content:center;color:#222}
  .metal--gold .metal__face{background:radial-gradient(circle at 50% 35%,#fff4d8,#f3cf86 70%,#d8a948)}
  .metal__name{font-family:"Open Sans",sans-serif;font-weight:600;font-size:11.5px;margin-top:6px}
  .metal__karat{font-family:"Open Sans",sans-serif;font-weight:600;font-size:27px;line-height:30px}
  .metal--1{left:32px}.metal--2{left:148px}.metal--3{left:262px}
  .orders{position:absolute;left:28px;top:262px;font-family:"Oswald",sans-serif;font-weight:600;
          font-size:37px;line-height:42px;white-space:nowrap}
  .orders__gold{color:var(--gold);display:block}
  .orders__white{color:var(--white);display:block}
  .no-min{position:absolute;left:26px;top:366px;font-family:"Oswald",sans-serif;font-weight:600;
          font-size:55px;line-height:64px;color:var(--gold);letter-spacing:1px;white-space:nowrap}
  .back-contacts{position:absolute;left:22px;top:453px;font-family:"Open Sans",sans-serif;
                 font-size:10.5px;color:#e8e8e8;line-height:18px}
  .back-contacts .contact-item{gap:5px}
  .back-divider{position:absolute;left:194px;top:454px;width:1px;height:32px;background:#aaa}
  .back-phone{position:absolute;left:204px;top:457px;display:flex;align-items:center;gap:7px;
              white-space:nowrap;font-family:"Oswald",sans-serif;font-weight:500;font-size:18px;color:var(--white)}
  .back__dot{left:522px;top:24px;width:30px;height:30px}
  .back__brand{left:452px;width:170px;top:72px;font-size:19px;letter-spacing:1.5px}
  .stamp{position:absolute;left:650px;top:31px;width:109px;height:101px;border:1px solid #333}
  .address-line{position:absolute;left:498px;width:261px;height:1px;background:#555}
</style>
</head>
<body>
<main class="canvas">

  <section class="card card--front" aria-label="Postcard front">
    <svg class="card__art" viewBox="0 0 787 506">
      <defs>
        <radialGradient id="charcoal-bg" cx="70%" cy="40%" r="80%">
          <stop offset="0" stop-color="#3a3a3a"/><stop offset="1" stop-color="#1e1e1e"/>
        </radialGradient>
        <linearGradient id="satin" x1="0" y1="0" x2="1" y2="1">
          <stop offset="0" stop-color="#e8dede"/><stop offset=".3" stop-color="#d52a3c"/>
          <stop offset=".7" stop-color="#b50f24"/><stop offset="1" stop-color="#8c0a1a"/>
        </linearGradient>
        <linearGradient id="gold-band" x1="0" y1="0" x2="1" y2="0">
          <stop offset="0" stop-color="#d99a00"/><stop offset=".5" stop-color="#ffd24a"/><stop offset="1" stop-color="#e6a800"/>
        </linearGradient>
        <radialGradient id="ring-gold" cx="50%" cy="40%" r="60%">
          <stop offset="0" stop-color="#fff7dc"/><stop offset="1" stop-color="#d9b25a"/>
        </radialGradient>
        <radialGradient id="ring-silver" cx="50%" cy="40%" r="60%">
          <stop offset="0" stop-color="#ffffff"/><stop offset="1" stop-color="#bdbdbd"/>
        </radialGradient>
        <radialGradient id="ring-rose" cx="50%" cy="40%" r="60%">
          <stop offset="0" stop-color="#ffffff"/><stop offset="1" stop-color="#e8cbbd"/>
        </radialGradient>
        <linearGradient id="bar" x1="0" y1="0" x2="0" y2="1">
          <stop offset="0" stop-color="#f2f2f2"/><stop offset="1" stop-color="#b8b8b8"/>
        </linearGradient>
      </defs>
      <rect width="787" height="506" fill="url(#charcoal-bg)"/>
      <path d="M0 0 H440 C505 140 470 330 220 506 H0 Z" fill="#c8c8c8"/>
      <path d="M0 0 H426 C492 140 456 330 206 506 H0 Z" fill="url(#gold-band)"/>
      <path role="img" aria-label="Photo of two wedding rings resting on red satin ribbon"
            d="M0 0 H390 C455 140 420 330 180 506 H0 Z" fill="url(#satin)"/>
      <g stroke="#ffffff" stroke-width="5">
        <circle role="img" aria-label="Photo of a hammered yellow gold band" cx="396" cy="232" r="52" fill="url(#ring-gold)"/>
        <circle role="img" aria-label="Photo of a rose gold twisted band" cx="348" cy="328" r="42" fill="url(#ring-rose)"/>
        <circle role="img" aria-label="Photo of a patterned white gold band" cx="288" cy="406" r="34" fill="url(#ring-silver)"/>
        <circle role="img" aria-label="Photo of a plain yellow gold band" cx="228" cy="468" r="30" fill="url(#ring-gold)"/>
      </g>
      <path d="M292 482 H787 V506 H272 Z" fill="url(#bar)"/>
    </svg>

    <span class="brand-dot front__dot"></span>
    <div class="brand front__brand">TOLVEK DESIGNS</div>
    <div class="since">Since 1979</div>

    <p class="tagline">FAST &amp; RELIABLE CONTRACTORS IN</p>
    <p class="script script--line1">The Wedding Ring</p>
    <p class="script script--line2">Industry</p>

    <div class="provide">WE PROVIDE</div>
    <ul class="services">
      <li>Swiss cutting</li>
      <li>Basic to complex finishes and designs</li>
      <li>Hand chasing/embossing and engraving</li>
      <li>Laser engraving</li>
      <li>Diamond setting</li>
    </ul>

    <div class="contact-bar">
      <span class="contact-item">
        <svg class="icon" viewBox="0 0 16 16" fill="none" stroke="#333" stroke-width="1.3"><circle cx="8" cy="8" r="6.5"/><ellipse cx="8" cy="8" rx="3" ry="6.5"/><path d="M1.5 8h13M3 4.5h10M3 11.5h10"/></svg>
        www.tolvekdesigns.example
      </span>
      <span class="sep"></span>
      <span class="contact-item">
        <svg class="icon" viewBox="0 0 16 16" fill="none" stroke="#333" stroke-width="1.3"><circle cx="8" cy="8" r="7"/><rect x="4" y="5.5" width="8" height="5.5"/><path d="M4 5.5l4 3 4-3"/></svg>
        info@tolvekdesigns.example
      </span>
      <span class="sep"></span>
      <span class="contact-item phone">
        <svg class="icon" viewBox="0 0 16 16" fill="#333"><path d="M3.5 1.5l2.5 0 1 3.5-1.7 1.2a8 8 0 0 0 4.5 4.5l1.2-1.7 3.5 1v2.5c0 .8-.7 1.5-1.5 1.5C7 14 2 9 2 3c0-.8.7-1.5 1.5-1.5z"/></svg>
        555 - 314- 9072
      </span>
    </div>
  </section>

  <section class="card card--back" aria-label="Postcard back">
    <svg class="card__art" viewBox="0 0 787 506">
      <defs>
        <radialGradient id="charcoal-back" cx="40%" cy="40%" r="80%">
          <stop offset="0" stop-color="#3a3a3a"/><stop offset="1" stop-color="#1e1e1e"/>
        </radialGradient>
        <linearGradient id="gold-band-back" x1="0" y1="0" x2="1" y2="0">
          <stop offset="0" stop-color="#d99a00"/><stop offset=".6" stop-color="#ffd24a"/><stop offset="1" stop-color="#e6a800"/>
        </linearGradient>
      </defs>
      <path d="M348 0 C470 90 510 260 480 360 C460 430 420 480 380 506 H0 V0 Z" fill="#cfcfcf"/>
      <path d="M338 0 C455 90 495 260 465 360 C445 430 405 480 362 506 H0 V0 Z" fill="url(#gold-band-back)"/>
      <path d="M325 0 C420 90 455 250 432 350 C415 420 385 475 345 506 H0 V0 Z" fill="url(#charcoal-back)"/>
    </svg>

    <h2 class="offer">
      <span class="offer__lead">Cutting And Finishing</span>
      <span class="offer__price">As Low As <em>$10</em> Per Piece</span>
    </h2>

    <div class="metal metal--1"><div class="metal__face"><span class="metal__name">PLATINUM</span><span class="metal__karat">10k</span></div></div>
    <div class="metal metal--2 metal--gold"><div class="metal__face"><span class="metal__name">PALLADIUM</span><span class="metal__karat">14k</span></div></div>
    <div class="metal metal--3"><div class="metal__face"><span class="metal__name">.935 SILVER</span><span class="metal__karat">18k</span></div></div>

    <p class="orders">
      <span class="orders__gold">VOLUME AND SPECIAL</span>
      <span class="orders__white">ORDERS ACCEPTED</span>
    </p>
    <p class="no-min">NO MINIMUMS</p>

    <div class="back-contacts">
      <div class="contact-item">
        <svg class="icon" viewBox="0 0 16 16" fill="none" stroke="#ddd" stroke-width="1.3"><circle cx="8" cy="8" r="6.5"/><ellipse cx="8" cy="8" rx="3" ry="6.5"/><path d="M1.5 8h13M3 4.5h10M3 11.5h10"/></svg>
        www.tolvekdesigns.example
      </div>
      <div class="contact-item">
        <svg class="icon" viewBox="0 0 16 16" fill="none" stroke="#ddd" stroke-width="1.3"><circle cx="8" cy="8" r="7"/><rect x="4" y="5.5" width="8" height="5.5"/><path d="M4 5.5l4 3 4-3"/></svg>
        info@tolvekdesigns.example
      </div>
    </div>
    <span class="back-divider"></span>
    <div class="back-phone">
      <svg class="icon" style="width:16px;height:16px" viewBox="0 0 16 16" fill="#eee"><path d="M3.5 1.5l2.5 0 1 3.5-1.7 1.2a8 8 0 0 0 4.5 4.5l1.2-1.7 3.5 1v2.5c0 .8-.7 1.5-1.5 1.5C7 14 2 9 2 3c0-.8.7-1.5 1.5-1.5z"/></svg>
      555 - 314- 9072
    </div>

    <span class="brand-dot back__dot"></span>
    <div class="brand back__brand">TOLVEK DESIGNS</div>
    <div class="stamp" aria-label="Stamp area"></div>
    <span class="address-line" style="top:301px"></span>
    <span class="address-line" style="top:368px"></span>
    <span class="address-line" style="top:436px"></span>
  </section>

</main>
</body>
</html>
```